Trade Show Banner "Brindlequay"

1.7' x 3' vertical banner to complement trade show booth panels (3-panel tabletop booth attached). The word file (attached) is for text and not meant to imply design. We manage homeowner and condo associations that are run by volunteer boards of directors who already have full-time jobs or who may have no training in how to run an organization. It can be highly stressful and not very rewarding. We want this poster/banner to convey that feeling of stress along with a hope for relief and relaxation. Our logo is attached. The full logo is the top one in the file. You may also want to use the triangle (attached) in addition to or instead of the logo. Our corporate fonts are attached. Please let me know if you need additional information or if you feel like there is too much copy or any other thoughts or comments you have.

Target Market(s)

Volunteer boards of directors for homeowner and condo associations--all ages, genders, races, occupations.

Industry/Entity Type

Property Management

Other font styles liked:
• "Copper Lantern" is part of a trademark and should be in Mistral with the green from our logo

Requirements
Must have
• Simple, easy to read, don't clash with booth design
Nice to have
• convey the tension of stress contrasted with the feeling of relaxation and relief.

```html
<!DOCTYPE html>
<html lang="en">
<head>
<meta charset="utf-8">
<title>The Art of Brindlequay for Board Members</title>
<link rel="stylesheet" href="https://fonts.googleapis.com/css2?family=Cabin+Condensed:wght@500;600;700&family=Itim&family=Lobster&family=Caveat:wght@500&family=Arimo:wght@700&display=swap">
<style>
  :root {
    --navy: #262a66;
    --green: #1d7a2c;
    --maroon: #7b1a1d;
    --ink: #3a3a3a;
    --band: #efefef;
    --paper: #ffffff;
  }
  * { box-sizing: border-box; margin: 0; padding: 0; }
  html, body { width: 680px; height: 1200px; overflow: hidden; background: var(--paper); }
  .banner { position: relative; width: 680px; height: 1200px; background: var(--paper); overflow: hidden; }

  .hero-photo {
    position: absolute; left: 0; top: 0; width: 680px; height: 300px;
    background:
      radial-gradient(ellipse 170px 220px at 420px 120px, #e8edf3 0%, rgba(232,237,243,0) 70%),
      radial-gradient(circle 34px at 430px 60px, #5d4a3c 0%, #5d4a3c 90%, rgba(93,74,60,0) 100%),
      linear-gradient(180deg, #dfe5ec 0%, #eef1f5 60%, #ffffff 100%);
  }
  .hero-photo::after {
    content: ""; position: absolute; inset: 0;
    background: linear-gradient(90deg, rgba(255,255,255,0.55) 0%, rgba(255,255,255,0.1) 60%, rgba(255,255,255,0.4) 100%);
  }

  .title { position: absolute; left: 30px; top: 84px; }
  .title-lead, .title-tail {
    font-family: "Arimo", Arial, sans-serif; font-weight: 700; color: var(--navy);
    line-height: 1;
  }
  .title-lead { font-size: 36px; }
  .title-brand {
    display: block; font-family: "Lobster", cursive; color: var(--green);
    font-size: 68px; line-height: 1; margin: 0 0 0 8px; letter-spacing: 1px;
    -webkit-text-stroke: 0; text-shadow: 0 0 1px #fff, 2px 2px 0 #fff, -2px -2px 0 #fff, 2px -2px 0 #fff, -2px 2px 0 #fff, 3px 4px 4px rgba(0,0,0,0.35);
  }
  .title-tail { font-size: 33px; margin-top: 4px; }

  .stress-list { position: absolute; left: 0; top: 318px; width: 680px; }
  .stress-row {
    background: linear-gradient(90deg, var(--band) 0%, var(--band) 55%, rgba(239,239,239,0) 100%);
    padding: 18px 0 14px 38px; margin-bottom: 6px;
  }
  .stress-label {
    font-family: "Cabin Condensed", sans-serif; font-weight: 600; color: var(--maroon);
    font-size: 20px; letter-spacing: 0.1px; line-height: 1.2;
  }
  .stress-relief {
    font-family: "Itim", cursive; color: var(--ink); font-size: 22px; line-height: 33px;
    margin-top: 16px; padding-right: 40px;
  }
  .relax {
    font-family: "Lobster", cursive; color: var(--green); font-size: 25px; letter-spacing: 0.5px;
  }
  .trademark { font-family: "Caveat", cursive; color: var(--green); font-size: 22px; }

  .row-1 { height: 112px; }
  .row-2 { height: 112px; }
  .row-3 { height: 112px; }
  .row-4 { height: 152px; }
  .row-5 { height: 210px; }

  .call-to-action {
    position: absolute; left: 38px; top: 1078px;
    font-family: "Cabin Condensed", sans-serif; font-weight: 600; color: var(--navy);
    font-size: 30px; line-height: 1.35;
  }
  .call-to-action .relax { font-size: 30px; }

  .company-mark {
    position: absolute; left: 432px; top: 1086px; width: 222px;
    display: flex; align-items: center; gap: 10px;
  }
  .company-mark .mark-square { width: 40px; height: 40px; background: var(--maroon); flex: none; }
  .company-name {
    font-family: "Cabin Condensed", sans-serif; font-weight: 500; color: var(--navy);
    font-size: 19px; line-height: 1.15; letter-spacing: 0.6px; text-transform: uppercase;
  }
</style>
</head>
<body>
<main class="banner">
  <div class="hero-photo" role="img" aria-label="Photo of a relaxed man in a white shirt leaning back in an office chair, hands behind his head"></div>

  <h1 class="title">
    <span class="title-lead">The Art of</span>
    <span class="title-brand">Brindlequay</span>
    <span class="title-tail">for Board Members</span>
  </h1>

  <section class="stress-list">
    <div class="stress-row row-1">
      <p class="stress-label">Stress: THE BOARD HAS TOO MUCH WORK TO DO</p>
      <p class="stress-relief"><span class="relax">Relax...</span>and let us do the work.</p>
    </div>
    <div class="stress-row row-2">
      <p class="stress-label">Stress: YOUR COMMUNITY HAS “ISSUES”.</p>
      <p class="stress-relief"><span class="relax">Relax...</span>and let us give you a <span class="trademark">Copper Lantern.</span></p>
    </div>
    <div class="stress-row row-3">
      <p class="stress-label">Stress: YOUR MEMBERS CANNOT PAY ONLINE.</p>
      <p class="stress-relief"><span class="relax">Relax...</span>we’ll give your members multiple ways to pay.</p>
    </div>
    <div class="stress-row row-4">
      <p class="stress-label">Stress: COMMUNICATION IS POOR OR INCONSISTENT.</p>
      <p class="stress-relief"><span class="relax">Relax...</span>we’ll keep you informed with a robust online portal, chock full of information.</p>
    </div>
    <div class="stress-row row-5">
      <p class="stress-label">Stress: YOUR DELINQUENCIES ARE HIGH.</p>
      <p class="stress-relief"><span class="relax">Relax...</span>as a licensed collection agency, we have developed an effective collections program that works in tandem with your collections attorney. Plus, we can report to the credit bureau!</p>
    </div>
  </section>

  <p class="call-to-action">COME IN TO TALK AND<br>START <span class="relax">Relaxing</span> TODAY!</p>

  <div class="company-mark">
    <span class="mark-square"></span>
    <span class="company-name">Halvorsen<br>Management, Inc.</span>
  </div>
</main>
</body>
</html>
```